Business card for our start up Automotive Shop

Clean business card design for our new automotive shop Brightline Motor Works. This card will be the template for all of our staff member including technicians and service advisors.

Brightline Motor Works is an automotive service shop catering to US domestic and asian import vehicles. We are a service and maintenance full service facility. Our aim is to provide the best quality workmanship and the best customer service experience in our industry.

Our target market are young professionals to people with families. We are not targeting a younger audience or the car modification scene. The card should be appealing to women of the 30+ age demographic.

We are a shop of younger professionals instead of an older crowd. The card design should reflect as such.

Target Market(s)

30+ Female demographic and 30+ male.

Industry/Entity Type

Automotive

Contact Information for Business Card

Must be clean and appealing to clients. Large enough and easy to read print.

Font styles to use
Sans Serif

Colors
f78f20
ffffff
b2b2b2
dddddd

Requirements
Must have
• Address, website and phone number
• 42-15 58th Ave
• Cedar Hollow NY 11462
• (718) 402-3917
• brightlinemotorworks.com
• There must be an area to add a Name and e-mail address for personalization purposes.
Nice to have
• Back of the card should have website.
• I would also like to incorporate yelp, google+, Facebook, and instagram widgets. Will add the exact pages but everything can be @ or / brightlinemotorworks
• That can be added on the back of the card.

```html
<!DOCTYPE html>
<html lang="en">
<head>
<meta charset="utf-8">
<title>Brightline Motor Works — Business Card</title>
<link rel="stylesheet" href="https://fonts.googleapis.com/css2?family=Exo+2:wght@500;600;700&display=swap">
<style>
  :root {
    --brand-orange: #f08a26;
    --brand-orange-deep: #e27d1c;
    --ink-light: #f3ece2;
    --backdrop: #e7e2db;
    --frame-grey: #dddddd;
  }
  * { margin: 0; padding: 0; box-sizing: border-box; }
  html, body {
    width: 1200px; height: 1046px; overflow: hidden;
    background: var(--backdrop);
    font-family: "Exo 2", Arial, sans-serif;
  }
  .card {
    position: absolute; left: 152px; top: 292px;
    width: 944px; height: 512px;
    border-radius: 18px;
    background: linear-gradient(100deg, var(--brand-orange) 0%, var(--brand-orange-deep) 100%);
    color: var(--ink-light);
    overflow: hidden;
  }
  .brand {
    position: absolute; left: 80px; top: 70px;
    display: flex; align-items: center; gap: 18px;
  }
  .brand-dot {
    width: 76px; height: 76px; border-radius: 50%;
    border: 7px solid var(--ink-light);
  }
  .brand-name {
    font-weight: 600; text-transform: uppercase; line-height: 1;
  }
  .brand-name .line-1 { display: block; font-size: 36px; letter-spacing: 1px; }
  .brand-name .line-2 { display: block; font-size: 19px; letter-spacing: 9px; margin-top: 8px; }
  .person { position: absolute; left: 92px; top: 270px; }
  .person-name { font-size: 32px; font-weight: 700; letter-spacing: 1px; text-transform: uppercase; }
  .person-role { font-size: 25px; font-weight: 500; letter-spacing: 0.5px; margin-top: 2px; }
  .contact { position: absolute; left: 92px; top: 362px; font-size: 20px; font-weight: 500; letter-spacing: 1.2px; }
  .contact-row { display: flex; align-items: center; gap: 14px; height: 30px; }
  .contact-row svg { width: 16px; height: 18px; flex: none; }
  .address { margin-top: 8px; line-height: 30px; }
  .social { position: absolute; left: 340px; top: 430px; font-size: 20px; font-weight: 500; letter-spacing: 1.2px; }
  .social-icons { display: flex; gap: 8px; margin-bottom: 8px; }
  .social-icons span { width: 16px; height: 16px; border-radius: 3px; background: var(--ink-light); }
  .emblem { position: absolute; left: 604px; top: 28px; width: 464px; height: 464px; }
</style>
</head>
<body>
  <div class="card">
    <div class="brand">
      <div class="brand-dot"></div>
      <div class="brand-name">
        <span class="line-1">Brightline</span>
        <span class="line-2">Motor Works</span>
      </div>
    </div>

    <div class="person">
      <div class="person-name">Dana Whitfield</div>
      <div class="person-role">Founder</div>
    </div>

    <div class="contact">
      <div class="contact-row">
        <svg viewBox="0 0 16 18"><rect x="3" y="1" width="10" height="16" rx="2" fill="none" stroke="#f3ece2" stroke-width="1.6"/></svg>
        <span>(718) 402-3917</span>
      </div>
      <div class="contact-row">
        <svg viewBox="0 0 16 18"><circle cx="7" cy="8" r="5" fill="none" stroke="#f3ece2" stroke-width="2"/><line x1="10.5" y1="11.5" x2="15" y2="16" stroke="#f3ece2" stroke-width="2.2"/></svg>
        <span>brightlinemotorworks.com</span>
      </div>
      <div class="address">42-15 58th Ave<br>Cedar Hollow NY 11462</div>
    </div>

    <div class="social">
      <div class="social-icons"><span></span><span></span><span></span></div>
      <div class="social-handle">brightlinemotorworks</div>
    </div>

    <svg class="emblem" viewBox="0 0 464 464" aria-hidden="true">
      <circle cx="232" cy="232" r="224" fill="none" stroke="#f3ece2" stroke-width="10"/>
    </svg>
  </div>
</body>
</html>
```